Real estate business card

I need a business card for my real estate company. I help clients buy and sell properties. I would like to keep the design very simple and professional. I would like the design to convey professionalism, safety and trust. I prefer no graphics but a simple logo design would be nice if that is part of what you do.
Updates

Please keep the designs simple. No high-rise buildings please. 

Reason: My design has not been finalized.

Target Market(s)

Age group 30-60 mostly affluent

Industry/Entity Type

Real Estate

Contact Information for Business Card

Velmont Realtors
Howard Prisk, Broker
4153 Marlow Ave. #226, La Crescenta, CA 91207

Requirements
Nice to have
• Logo can be combination of my initials HP or just Z or a simple geometric shape? Please see "Desig Ideas" attachment. No pics of houses or shaking hands, dollar bills, $, %, etc...
Please use fonts similar to Helvetica for a clean, modern look (think Northern European design, simple, clean yet bold)

Also use font colors such as blue, grey in different shades. Use pastel colors if better.

```html
<!DOCTYPE html>
<html lang="en">
<head>
<meta charset="utf-8">
<title>Velmont Realtors – Business Card</title>
<link href="https://fonts.googleapis.com/css2?family=Arimo:wght@400;700&display=swap" rel="stylesheet">
<style>
  :root {
    --page: #ffffff;
    --card: #000000;
    --gold: #b8893a;
    --gold-soft: #a9813f;
  }
  * { margin: 0; padding: 0; box-sizing: border-box; }
  html, body {
    width: 1096px;
    height: 1200px;
    overflow: hidden;
    background: var(--page);
    font-family: "Arimo", Helvetica, Arial, sans-serif;
  }
  .canvas {
    position: relative;
    width: 1096px;
    height: 1200px;
  }
  .card {
    position: absolute;
    left: 208px;
    width: 680px;
    height: 368px;
    background: var(--card);
    color: var(--gold);
  }
  .card--front { top: 193px; }
  .card--back  { top: 642px; }

  .brand {
    position: absolute;
    display: flex;
    flex-direction: column;
    align-items: center;
    text-align: center;
  }
  .card--front .brand { left: 90px; top: 118px; width: 190px; }
  .card--back  .brand { left: 245px; top: 120px; width: 190px; }

  .brand__mark {
    width: 26px;
    height: 26px;
    background: var(--gold);
    margin-bottom: 22px;
  }
  .brand__name {
    font-weight: 400;
    font-size: 30px;
    letter-spacing: 5px;
    line-height: 1;
    padding-left: 5px;
  }
  .brand__sub {
    font-weight: 400;
    font-size: 10px;
    letter-spacing: 8px;
    margin-top: 13px;
    padding-left: 8px;
  }

  .divider {
    position: absolute;
    left: 339px;
    top: 60px;
    width: 2px;
    height: 268px;
    background: var(--gold);
  }

  .contact {
    position: absolute;
    left: 384px;
    top: 70px;
    font-size: 15.5px;
    line-height: 21px;
    color: var(--gold);
  }
  .contact__name {
    font-size: 24px;
    letter-spacing: 1.5px;
    line-height: 1;
  }
  .contact__role {
    font-size: 9px;
    font-weight: 700;
    letter-spacing: 5px;
    margin-top: 10px;
  }
  .contact__group { margin-top: 22px; }
  .contact__group + .contact__group { margin-top: 16px; }
  .contact p { white-space: nowrap; }
</style>
</head>
<body>
<main class="canvas">

  <section class="card card--front" aria-label="Business card front">
    <div class="brand">
      <span class="brand__mark" aria-hidden="true"></span>
      <span class="brand__name">VELMONT</span>
      <span class="brand__sub">REALTORS</span>
    </div>

    <span class="divider" aria-hidden="true"></span>

    <div class="contact">
      <p class="contact__name">HOWARD PRISK</p>
      <p class="contact__role">BROKER</p>

      <div class="contact__group">
        <p>phone: 818-555-0142</p>
        <p>fax: 626-555-0178</p>
      </div>
      <div class="contact__group">
        <p>hprisk@velmontrealtors.com</p>
        <p>www.velmontrealtors.com</p>
      </div>
      <div class="contact__group">
        <p>CA BRE 01473805</p>
      </div>
      <div class="contact__group">
        <p>4153 Marlow Ave. #226,</p>
        <p>La Crescenta, CA 91207</p>
      </div>
    </div>
  </section>

  <section class="card card--back" aria-label="Business card back">
    <div class="brand">
      <span class="brand__mark" aria-hidden="true"></span>
      <span class="brand__name">VELMONT</span>
      <span class="brand__sub">REALTORS</span>
    </div>
  </section>

</main>
</body>
</html>
```